Three diagrams for an academic paper

I need professional-looking versions of three diagrams for an academic paper. I am uploading JPEGs of each diagram drafted in Brindlewave Docs. I need completely new versions that look much better.

Some detailed requirements:
- Professional styling - must be clearly superior to the ‘stick-figure’ example images and obviously not from powerpoint, etc.
- Must be a coordinated style across all three illustrations.
- Note that a mini-version of figure 2 appears in figure 3 (within the database image)
- I need very high resolution, suitable for a manuscript
- May need some text changes at short notice (anticipate 2 small updates to text)

Target Market(s)

Academics

Industry/Entity Type

Brindlewave

Font styles to use
Sans Serif

Colors

Designer to choose colors to be used in the design.

Requirements
Must have
• Don't look like powerpoint

```html
<!DOCTYPE html>
<html lang="en">
<head>
<meta charset="utf-8">
<title>Structured Journalism Pipeline</title>
<link href="https://fonts.googleapis.com/css2?family=Open+Sans:wght@600;700;800&display=swap" rel="stylesheet">
<style>
  :root {
    --ink: #111111;
    --paper: #ffffff;
    --card: #d3d4d6;
    --node-light: #ffffff;
    --node-dark: #6e6e72;
    --steel-dark: #4a4a4d;
    --steel-light: #f3f3f3;
    --glow-deep: #0a5f92;
    --glow-bright: #56d4f7;
    --graph-top: #fbf3f6;
    --graph-bottom: #efe6d8;
  }
  html, body {
    margin: 0;
    padding: 0;
    width: 1200px;
    height: 1200px;
    overflow: hidden;
    background: var(--paper);
  }
  .canvas { display: block; width: 1200px; height: 1200px; }
  .section-title { font-family: "Open Sans", sans-serif; font-weight: 700; font-size: 32px; fill: var(--ink); }
  .node-label { font-family: "Open Sans", sans-serif; font-weight: 600; font-size: 15px; fill: var(--ink); text-anchor: middle; }
  .db-caption { font-family: "Open Sans", sans-serif; font-weight: 700; font-size: 24px; fill: var(--ink); text-anchor: middle; }
  .axis-label { font-family: "Open Sans", sans-serif; font-weight: 700; font-size: 20px; fill: var(--paper); text-anchor: middle; dominant-baseline: central; }
  .flow-arrow { fill: var(--ink); }
  .node { stroke: none; }
  .doc-card { fill: var(--card); stroke: var(--ink); stroke-width: 0.8; }
  .doc-text-box { fill: var(--paper); stroke: var(--ink); stroke-width: 0.5; }
  .doc-text { font-family: "Open Sans", sans-serif; font-size: 3.4px; font-weight: 600; fill: var(--ink); }
  .graph-slot { fill: url(#graph-tone); stroke: #777; stroke-width: 0.5; }
  .structure-arrow { stroke: var(--paper); stroke-width: 3; }
</style>
</head>
<body>
<svg class="canvas" viewBox="0 0 1200 1200" xmlns="http://www.w3.org/2000/svg">
  <defs>
    <radialGradient id="node-fill" cx="50%" cy="45%" r="55%">
      <stop offset="0" stop-color="var(--node-light)"/>
      <stop offset="0.45" stop-color="#d6d6d8"/>
      <stop offset="1" stop-color="var(--node-dark)"/>
    </radialGradient>
    <linearGradient id="steel" x1="0" y1="0" x2="1" y2="0">
      <stop offset="0" stop-color="var(--steel-dark)"/>
      <stop offset="0.3" stop-color="var(--steel-light)"/>
      <stop offset="0.55" stop-color="#a5a5a8"/>
      <stop offset="0.8" stop-color="#707073"/>
      <stop offset="1" stop-color="var(--steel-dark)"/>
    </linearGradient>
    <linearGradient id="glow" x1="0" y1="0" x2="1" y2="0">
      <stop offset="0" stop-color="var(--glow-deep)"/>
      <stop offset="0.4" stop-color="var(--glow-bright)"/>
      <stop offset="0.7" stop-color="#2aa7dc"/>
      <stop offset="1" stop-color="var(--glow-deep)"/>
    </linearGradient>
    <linearGradient id="graph-tone" x1="0" y1="0" x2="0" y2="1">
      <stop offset="0" stop-color="var(--graph-top)"/>
      <stop offset="1" stop-color="var(--graph-bottom)"/>
    </linearGradient>
    <filter id="soft-shadow" x="-10%" y="-10%" width="120%" height="130%">
      <feDropShadow dx="0" dy="4" stdDeviation="4" flood-color="#000" flood-opacity="0.35"/>
    </filter>
  </defs>

  <!-- headings -->
  <text class="section-title" x="98" y="164">DATA SOURCES</text>
  <text class="section-title" x="1104" y="166" text-anchor="end">NEWS PRODUCTS</text>

  <!-- incoming arrows -->
  <g class="flow-arrow">
    <polygon transform="translate(284,272) rotate(45)" points="0,-8 227,-2.5 227,-9 249,0 227,9 227,2.5 0,8"/>
    <polygon transform="translate(292,380) rotate(31.8)" points="0,-8 176,-2.5 176,-9 198,0 176,9 176,2.5 0,8"/>
    <polygon transform="translate(294,504) rotate(13.5)" points="0,-8 149,-2.5 149,-9 171,0 149,9 149,2.5 0,8"/>
    <polygon transform="translate(294,620) rotate(-10.9)" points="0,-8 147,-2.5 147,-9 169,0 147,9 147,2.5 0,8"/>
    <polygon transform="translate(294,748) rotate(-17.4)" points="0,-8 152,-2.5 152,-9 174,0 152,9 152,2.5 0,8"/>
    <polygon transform="translate(294,872) rotate(-31)" points="0,-8 172,-2.5 172,-9 194,0 172,9 172,2.5 0,8"/>
    <polygon transform="translate(286,988) rotate(-44)" points="0,-8 220,-2.5 220,-9 242,0 220,9 220,2.5 0,8"/>
  </g>

  <!-- outgoing arrows -->
  <g class="flow-arrow">
    <polygon transform="translate(730,432) rotate(-44.3)" points="0,-8 207,-2.5 207,-9 229,0 207,9 207,2.5 0,8"/>
    <polygon transform="translate(730,472) rotate(-28.6)" points="0,-8 158,-2.5 158,-9 180,0 158,9 158,2.5 0,8"/>
    <polygon transform="translate(730,552) rotate(-15.6)" points="0,-8 142,-2.5 142,-9 164,0 142,9 142,2.5 0,8"/>
    <polygon transform="translate(730,592) rotate(14.2)" points="0,-8 141,-2.5 141,-9 163,0 141,9 141,2.5 0,8"/>
    <polygon transform="translate(730,696) rotate(20.8)" points="0,-8 147,-2.5 147,-9 169,0 147,9 147,2.5 0,8"/>
    <polygon transform="translate(730,780) rotate(29.1)" points="0,-8 159,-2.5 159,-9 181,0 159,9 159,2.5 0,8"/>
    <polygon transform="translate(730,820) rotate(46)" points="0,-8 211,-2.5 211,-9 233,0 211,9 211,2.5 0,8"/>
  </g>

  <!-- data source nodes -->
  <g class="sources">
    <ellipse class="node" cx="217" cy="250" rx="79" ry="61" fill="url(#node-fill)"/>
    <text class="node-label" x="217" y="255">Sensors</text>
    <ellipse class="node" cx="217" cy="374" rx="79" ry="61" fill="url(#node-fill)"/>
    <text class="node-label" x="217" y="370">Existing<tspan x="217" dy="19">datasets</tspan></text>
    <ellipse class="node" cx="217" cy="500" rx="79" ry="61" fill="url(#node-fill)"/>
    <text class="node-label" x="217" y="499">Manual data<tspan x="217" dy="19">entry</tspan></text>
    <ellipse class="node" cx="217" cy="626" rx="79" ry="61" fill="url(#node-fill)"/>
    <text class="node-label" x="217" y="616">Manual<tspan x="217" dy="19">annotation</tspan><tspan x="217" dy="19">of text</tspan></text>
    <ellipse class="node" cx="217" cy="752" rx="79" ry="61" fill="url(#node-fill)"/>
    <text class="node-label" x="217" y="730">Controlled<tspan x="217" dy="19">natural</tspan><tspan x="217" dy="19">language</tspan><tspan x="217" dy="19">authoring</tspan></text>
    <ellipse class="node" cx="217" cy="878" rx="79" ry="61" fill="url(#node-fill)"/>
    <text class="node-label" x="217" y="870">Automated<tspan x="217" dy="19">annotation</tspan><tspan x="217" dy="19">of text</tspan></text>
    <ellipse class="node" cx="217" cy="1004" rx="79" ry="61" fill="url(#node-fill)"/>
    <text class="node-label" x="217" y="991">Automated<tspan x="217" dy="19">data extraction</tspan><tspan x="217" dy="19">or assembly</tspan></text>
  </g>

  <!-- news product nodes -->
  <g class="products">
    <ellipse class="node" cx="968" cy="250" rx="79" ry="61" fill="url(#node-fill)"/>
    <text class="node-label" x="968" y="239">Conversational<tspan x="968" dy="19">interfaces</tspan><tspan x="968" dy="19">(News Bots)</tspan></text>
    <ellipse class="node" cx="968" cy="374" rx="79" ry="61" fill="url(#node-fill)"/>
    <text class="node-label" x="968" y="373">Automatically<tspan x="968" dy="19">written articles</tspan></text>
    <ellipse class="node" cx="968" cy="500" rx="79" ry="61" fill="url(#node-fill)"/>
    <text class="node-label" x="968" y="486">Authored<tspan x="968" dy="19">articles</tspan><tspan x="968" dy="19">(via analysis)</tspan></text>
    <ellipse class="node" cx="968" cy="626" rx="79" ry="61" fill="url(#node-fill)"/>
    <text class="node-label" x="968" y="626">Graphics and<tspan x="968" dy="19">visualizations</tspan></text>
    <ellipse class="node" cx="968" cy="752" rx="79" ry="61" fill="url(#node-fill)"/>
    <text class="node-label" x="968" y="746">Texteme-based<tspan x="968" dy="19">news products</tspan><tspan x="968" dy="19">(cards, etc)</tspan></text>
    <ellipse class="node" cx="968" cy="878" rx="79" ry="61" fill="url(#node-fill)"/>
    <text class="node-label" x="968" y="866">Quantitative<tspan x="968" dy="19">news products</tspan><tspan x="968" dy="19">(totals, tables)</tspan></text>
    <ellipse class="node" cx="968" cy="1004" rx="79" ry="61" fill="url(#node-fill)"/>
    <text class="node-label" x="968" y="991">Other<tspan x="968" dy="19">computable</tspan><tspan x="968" dy="19">news products</tspan></text>
  </g>

  <!-- database stack -->
  <g class="database">
    <rect x="480" y="494" width="224" height="28" fill="url(#glow)"/>
    <rect x="480" y="612" width="224" height="28" fill="url(#glow)"/>
    <rect x="480" y="728" width="224" height="28" fill="url(#glow)"/>
    <rect x="460" y="404" width="270" height="92" fill="url(#steel)" filter="url(#soft-shadow)"/>
    <rect x="460" y="520" width="270" height="94" fill="url(#steel)" filter="url(#soft-shadow)"/>
    <rect x="460" y="636" width="270" height="94" fill="url(#steel)" filter="url(#soft-shadow)"/>
    <rect x="460" y="752" width="270" height="94" fill="url(#steel)" filter="url(#soft-shadow)"/>

    <!-- document cards, from text to structure -->
    <g class="doc">
      <rect class="doc-card" x="544" y="418" width="96" height="76"/>
      <rect class="doc-text-box" x="546" y="420" width="48" height="72"/>
      <text class="doc-text" x="548" y="425">Council votes to<tspan x="548" dy="6.6">extend transit</tspan><tspan x="548" dy="6.6">funding for the</tspan><tspan x="548" dy="6.6">coming fiscal</tspan><tspan x="548" dy="6.6">year after long</tspan><tspan x="548" dy="6.6">debate among</tspan><tspan x="548" dy="6.6">members and</tspan><tspan x="548" dy="6.6">local residents</tspan><tspan x="548" dy="6.6">over route</tspan><tspan x="548" dy="6.6">changes and fares</tspan></text>
    </g>
    <g class="doc">
      <rect class="doc-card" x="544" y="502" width="96" height="78"/>
      <rect class="doc-text-box" x="546" y="504" width="46" height="70"/>
      <text class="doc-text" x="548" y="509">Council votes to<tspan x="548" dy="7">extend transit</tspan><tspan x="548" dy="7">funding for the</tspan><tspan x="548" dy="7">coming fiscal</tspan><tspan x="548" dy="7">year after long</tspan><tspan x="548" dy="7">debate among</tspan><tspan x="548" dy="7">members and</tspan><tspan x="548" dy="7">local residents</tspan><tspan x="548" dy="7">over fares</tspan></text>
      <rect class="graph-slot" x="595" y="505" width="40" height="27" role="img" aria-label="Small knowledge graph of linked story entities"/>
    </g>
    <g class="doc">
      <rect class="doc-card" x="544" y="587" width="96" height="79"/>
      <rect class="doc-text-box" x="546" y="589" width="46" height="44"/>
      <text class="doc-text" x="548" y="594">Council votes to<tspan x="548" dy="7">extend transit</tspan><tspan x="548" dy="7">funding for the</tspan><tspan x="548" dy="7">coming fiscal</tspan><tspan x="548" dy="7">year after</tspan><tspan x="548" dy="7">debate</tspan></text>
      <rect class="graph-slot" x="595" y="590" width="40" height="27" role="img" aria-label="Small knowledge graph of linked story entities"/>
    </g>
    <g class="doc">
      <rect class="doc-card" x="544" y="672" width="96" height="77"/>
      <rect class="doc-text-box" x="546" y="674" width="46" height="26"/>
      <text class="doc-text" x="548" y="679">Council votes to<tspan x="548" dy="7">extend transit</tspan><tspan x="548" dy="7">funding</tspan></text>
      <rect class="graph-slot" x="595" y="675" width="40" height="27" role="img" aria-label="Small knowledge graph of linked story entities"/>
    </g>
    <g class="doc">
      <rect class="doc-card" x="544" y="757" width="96" height="78"/>
      <rect class="graph-slot" x="595" y="760" width="40" height="27" role="img" aria-label="Small knowledge graph of linked story entities"/>
    </g>

    <!-- structure axis -->
    <line class="structure-arrow" x1="512" y1="456" x2="512" y2="796"/>
    <polygon points="505,792 519,792 512,810" fill="var(--paper)"/>
    <text class="axis-label" transform="translate(501,624) rotate(-90)">More Structure</text>
    <line class="structure-arrow" x1="666" y1="810" x2="666" y2="470"/>
    <polygon points="659,474 673,474 666,456" fill="var(--paper)"/>
    <text class="axis-label" transform="translate(678,624) rotate(90)">Less Structure</text>
  </g>

  <text class="db-caption" x="596" y="893">Database of<tspan x="596" dy="27">Structured</tspan><tspan x="596" dy="27">Journalistic</tspan><tspan x="596" dy="27">Knowledge</tspan></text>
</svg>
</body>
</html>
```